Automotive component supplier needs a business card design

We need a business card design for our company called Velmar Global Components Ltd based in the UK. We are a supplier of interior and exterior components to premium car manufacturers such as Corvane Hale, Durrant Fyfe, Maxtorn and Valdessimo. We would like to see a modern business card design that uses the colour blue.

Target Market(s)

Premium automotive car manufacturers.

Industry/Entity Type

Automotive

Contact Information for Business Card

Company Name : Velmar Global Components Limited
Address: 17 Tamsey Yard, Upper Drisk, Warwick, CV31 8RJ, United Kingdom
Web Address : www.velmarparts-example.co.uk

Font styles to use
Other font styles liked:
• Helvetica

Colors
3176b5
0255a3
85acd3
cfdeed
cee9f5
85cae6
34a6d7
0692cd
9bcb3c

Requirements
Must have
• Clear company logo and a mixture of blue colours.
Nice to have
• A high quality modern image.
Should not have
• Multiple colours.

```html
<!DOCTYPE html>
<html lang="en">
<head>
<meta charset="utf-8">
<title>Velmar Global Components – Business Card</title>
<link rel="stylesheet" href="https://fonts.googleapis.com/css2?family=Jost:wght@400;500;700&family=Carlito&display=swap">
<style>
  :root {
    --backdrop: #0a0b0d;
    --card-blue: #0b91c9;
    --ink: #ffffff;
  }
  * { box-sizing: border-box; margin: 0; padding: 0; }
  html, body {
    width: 1200px; height: 1200px; overflow: hidden;
    background: var(--backdrop);
  }
  .canvas { position: relative; width: 1200px; height: 1200px; }
  .card {
    position: absolute; width: 840px; height: 480px;
    background: var(--card-blue); color: var(--ink);
  }
  .card--front { left: 178px; top: 109px; }
  .card--back { left: 182px; top: 610px; }

  .brand {
    position: absolute; left: 0; right: 0; top: 158px;
    display: flex; flex-direction: column; align-items: center;
    font-family: "Jost", sans-serif; color: var(--ink);
  }
  .brand__name { font-size: 122px; font-weight: 700; line-height: 0.95; letter-spacing: 4px; }
  .brand__tagline {
    font-size: 30px; font-weight: 400; letter-spacing: 7px;
    margin-top: 16px; padding-left: 7px;
  }

  .person {
    position: absolute; left: 0; width: 354px; top: 218px;
    text-align: center; font-family: "Jost", sans-serif; color: var(--ink);
  }
  .person__name { font-size: 27px; font-weight: 500; line-height: 1.1; }
  .person__name strong { font-weight: 700; }
  .person__role { font-size: 20px; font-weight: 500; margin-top: 2px; }

  .divider {
    position: absolute; left: 352px; top: 46px;
    width: 3px; height: 388px; background: var(--ink);
  }

  .contacts {
    position: absolute; left: 406px; top: 0; right: 0;
    font-family: "Carlito", sans-serif; font-size: 23px; color: var(--ink);
    list-style: none;
  }
  .contacts__item { position: absolute; left: 0; display: flex; align-items: center; gap: 10px; white-space: nowrap; }
  .contacts__item--address { top: 118px; align-items: flex-start; line-height: 30px; }
  .contacts__item--fax { top: 196px; }
  .contacts__item--phone { top: 240px; }
  .contacts__item--email { top: 282px; }
  .contacts__item--web { top: 326px; }
  .icon { width: 36px; height: 36px; flex: none; }
  .contacts__item--address .icon { margin-top: 6px; }
</style>
</head>
<body>
<main class="canvas">
  <section class="card card--front" aria-label="Card front">
    <div class="brand">
      <span class="brand__name">VELMAR</span>
      <span class="brand__tagline">GLOBAL COMPONENTS</span>
    </div>
  </section>

  <section class="card card--back" aria-label="Card back">
    <div class="person">
      <p class="person__name">DORRAN <strong>KESWICK</strong></p>
      <p class="person__role">GRAPHIX DESIGNER</p>
    </div>
    <div class="divider"></div>
    <ul class="contacts">
      <li class="contacts__item contacts__item--address">
        <svg class="icon" viewBox="0 0 36 36" fill="none" stroke="#fff" stroke-width="2"><circle cx="18" cy="18" r="16.5"/><path d="M18 28c-5-6-7-9-7-12a7 7 0 0 1 14 0c0 3-2 6-7 12z" fill="#fff" stroke="none"/><circle cx="18" cy="15.5" r="2.6" fill="var(--card-blue)" stroke="none"/></svg>
        <span>17 Tamsey Yard, Upper Drisk,<br>Warwick, CV31 8RJ, United Kingdom.</span>
      </li>
      <li class="contacts__item contacts__item--fax">
        <svg class="icon" viewBox="0 0 36 36" fill="none" stroke="#fff" stroke-width="2"><circle cx="18" cy="18" r="16.5"/><path d="M10 16c0-4 16-4 16 0v2h-4v-2h-8v2h-4z" fill="#fff" stroke="none"/><rect x="12" y="18" width="12" height="7" rx="1" fill="#fff" stroke="none"/></svg>
        <span>000. 123. 4567</span>
      </li>
      <li class="contacts__item contacts__item--phone">
        <svg class="icon" viewBox="0 0 36 36" fill="none" stroke="#fff" stroke-width="2"><circle cx="18" cy="18" r="16.5"/><path d="M12 10l3.5-1 2 5-2.2 1.6a11 11 0 0 0 5 5l1.6-2.2 5 2-1 3.5c-8 1-15-6-13.9-13.9z" fill="#fff" stroke="none"/></svg>
        <span>000. 123. 4567</span>
      </li>
      <li class="contacts__item contacts__item--email">
        <svg class="icon" viewBox="0 0 36 36" fill="none" stroke="#fff" stroke-width="2"><circle cx="18" cy="18" r="16.5"/><rect x="10.5" y="13" width="15" height="10" rx="1" fill="#fff" stroke="none"/><path d="M11 13.5l7 5 7-5" stroke="var(--card-blue)" stroke-width="1.5"/></svg>
        <span>hello@velmarparts-example.co.uk</span>
      </li>
      <li class="contacts__item contacts__item--web">
        <svg class="icon" viewBox="0 0 36 36" fill="none" stroke="#fff" stroke-width="2"><circle cx="18" cy="18" r="16.5"/><circle cx="18" cy="18" r="9" stroke-width="1.6"/><ellipse cx="18" cy="18" rx="4" ry="9" stroke-width="1.4"/><path d="M9 18h18M10.5 13.5h15M10.5 22.5h15" stroke-width="1.4"/></svg>
        <span>www.velmarparts-example.co.uk</span>
      </li>
    </ul>
  </section>
</main>
</body>
</html>
```